Vantorix needs a newsletter to introduce our new test - Helix Balance Profile

I need a newsletter or email design to introduce a new test that my company has to offer called Helix Balance Profile. We are launching this genetic test to fitness centers, nutritionists, high end gyms, personal trainers and others. The genetic test looks at 5 genetic markers that are key to how each individual processes nutrients, carbohydrates etc and then provides a comprehensive report for the individual on specific diet plans, exercise regimens and their genetic results. The newsletter should be an exciting announcement of this new test and one that can easily be used via email or via attachments. I have attached some files which provide much more detail. The final design should communicate an opportunity for these potential customers to increase revenue, provide their members with an extraordinary personalized genetic test and to provide a value add to their current offerings.
Updates
Hi,
I forgot to upload a one page marketing piece that i had created as well as the logo for vantorix. Happy to provide just not sure how to upload them into the project
Target Market(s)
fitness centers, high end gyms, nutritionists, dieticians, personal trainers, health coaches
Colors
Designer to choose colors to be used in the design.
Look and feel
Each slider illustrates characteristics of the customer's brand and the style your logo design should communicate.

```html
<!DOCTYPE html>
<html lang="en">
<head>
<meta charset="utf-8">
<title>Vantorix – Genetic Testing for Weight Management</title>
<link rel="stylesheet" href="https://fonts.googleapis.com/css2?family=Crimson+Pro:wght@400;500&family=Open+Sans:wght@400;600&family=Arimo:wght@400;700&display=swap">
<style>
:root{
  --teal:#1fb8b4;
  --pie:#2ab5c7;
  --navy:#1a2568;
  --ink:#1d1d1d;
  --panel:#efefef;
  --panel-light:#f6f6f6;
  --rule:#c9c9c9;
  --white:#ffffff;
}
*{margin:0;padding:0;box-sizing:border-box}
html,body{width:713px;height:1200px;overflow:hidden;background:var(--white)}
body{position:relative;font-family:"Arimo",Arial,sans-serif;color:var(--ink)}
.abs{position:absolute}

/* hero */
.hero{left:56px;top:0;width:600px;height:294px;overflow:hidden}
.hero-photo{position:absolute;inset:0;background:linear-gradient(90deg,#e9ebea 0%,#dcdcdc 40%,#d9b7a6 62%,#e2c4b4 78%,#ccd0cf 100%)}
.brand{position:absolute;left:40px;top:86px;display:flex;align-items:center;gap:8px;font-family:"Crimson Pro",serif;font-weight:500;font-size:25px;color:var(--navy)}
.brand-dot{width:14px;height:14px;border-radius:50%;background:var(--teal)}
.hero-band{position:absolute;left:0;top:182px;width:600px;height:94px;background:linear-gradient(90deg,var(--teal) 0%,var(--teal) 55%,rgba(31,184,180,.55) 80%,rgba(31,184,180,.25) 100%)}
.hero-title{position:absolute;left:28px;top:186px;font-family:"Crimson Pro",serif;font-size:35px;line-height:40px;color:var(--white);font-weight:400}
.btn{display:flex;align-items:center;justify-content:center;background:var(--navy);color:var(--white);font-family:"Open Sans",sans-serif;border-radius:8px;text-decoration:none}
.btn-purchase{position:absolute;left:380px;top:207px;width:196px;height:44px;font-size:18px}

/* intro */
.intro{left:56px;top:294px;width:392px;height:310px;background:var(--panel)}
.intro-head{position:absolute;left:29px;top:36px;width:310px;font-family:"Crimson Pro",serif;font-weight:400;font-size:21px;line-height:26px;color:var(--navy)}
.intro-body{position:absolute;left:29px;top:159px;width:332px;font-size:13.6px;line-height:22px}
.stat{left:448px;top:294px;width:208px;height:310px;background:var(--panel-light)}
.pie-label{position:absolute;left:22px;top:38px;width:74px;text-align:center;font-family:"Crimson Pro",serif;color:var(--navy);font-size:14px;line-height:15px}
.stat-caption{position:absolute;left:0;top:222px;width:208px;text-align:center;font-family:"Crimson Pro",serif;font-size:13.5px;line-height:18px;color:var(--navy)}

/* learn */
.learn-photo{left:56px;top:640px;width:228px;height:141px;background:linear-gradient(135deg,#8c7a6c 0%,#c9b3a0 35%,#eeeeee 60%,#d5d7dc 100%)}
.learn{left:315px;top:638px;width:360px;font-size:14px;line-height:22px}
.learn ul{list-style:none;margin-top:9px}
.learn li{position:relative;padding-left:27px;width:340px}
.learn li::before{content:"";position:absolute;left:10px;top:7px;width:7px;height:7px;border-radius:50%;background:#666}

/* audience band */
.audience{left:56px;top:814px;width:600px;height:36px;background:var(--teal);color:var(--white);font-family:"Open Sans",sans-serif;font-size:12.4px;display:flex;align-items:center;justify-content:center}

/* report */
.report-text{left:56px;top:881px;width:430px;font-size:13.8px;line-height:22px}
.btn-sample{position:absolute;left:56px;top:984px;width:216px;height:37px;font-size:14px}
.report-thumb{left:509px;top:869px;width:147px;height:175px;background:#c6cbcb;padding:6px}
.report-page{width:100%;height:100%;background:var(--white)}

/* footer */
.footer-rule{left:56px;top:1090px;width:600px;height:1px;background:var(--rule)}
.footer{left:0;top:1109px;width:713px;text-align:center;font-size:11px;color:#333}
</style>
</head>
<body>

<header class="abs hero">
  <div class="hero-photo" role="img" aria-label="Woman measuring her waist with a yellow tape measure"></div>
  <div class="brand"><span class="brand-dot"></span>Vantorix</div>
  <div class="hero-band"></div>
  <h1 class="hero-title">Genetic Testing for<br>Weight Management</h1>
  <a class="btn btn-purchase">PURCHASE NOW</a>
</header>

<section class="abs intro">
  <h2 class="intro-head">Researchers can now determine how a person's genetic background determines their ability to lose or gain body weight.</h2>
  <p class="intro-body">The Helix Balance Profile incorporates the most scientifically robust obesity-linked gene research and technology to help you understand how your genes influence body weight, and the weight managment strategies most likely to be effective for your specific genetic make-up.</p>
</section>

<aside class="abs stat">
  <svg class="abs" style="left:0;top:0" width="208" height="220" viewBox="0 0 208 220" aria-label="Pie chart: genetic risk 86%, non-genetic risk 14%">
    <circle cx="108" cy="124" r="75" fill="var(--pie)" stroke="var(--navy)" stroke-width="1.2"/>
    <path d="M108 124 L108 49 A75 75 0 0 0 50.2 76.2 Z" fill="var(--white)" stroke="var(--navy)" stroke-width="1.2"/>
    <text x="93" y="92" text-anchor="middle" font-family="Crimson Pro, serif" font-size="15" fill="#555">14%</text>
    <text x="113" y="168" text-anchor="middle" font-family="Arimo, sans-serif" font-size="14" fill="#fff">Genetic Risk</text>
    <text x="111" y="185" text-anchor="middle" font-family="Arimo, sans-serif" font-size="14" font-weight="700" fill="#fff">86%</text>
  </svg>
  <div class="pie-label">NonGenetic<br>Risk</div>
  <p class="stat-caption">Genetics contributes<br>an esimated&nbsp; 40% to 86%<br>of variability in body weight<br>according to multiple studies.</p>
</aside>

<div class="abs learn-photo" role="img" aria-label="Hands reviewing a printed report with a pen"></div>
<section class="abs learn">
  <p>Through the <b>Helix Balance Profile</b>, you'll learn:</p>
  <ul>
    <li>The best diet plan for you based on your genetics</li>
    <li>How your genetics affect your eating habits</li>
    <li>How your genetics determine the way your body uses nutrients from food</li>
    <li>The exercise that works best for your body</li>
  </ul>
</section>

<nav class="abs audience">FITNESS CENTERS&nbsp; |&nbsp; NUTRITIONISTS&nbsp; |&nbsp; HIGH END GYMS&nbsp; |&nbsp; PERSONAL TRAINERS&nbsp; |&nbsp; OTHERS</nav>

<p class="abs report-text">The genetic test looks at 5 genetic markers that are key to how each individual processes nutrients, carbohydrates etc and then provides a comprehensive report for the individual on specific diet plans, exercise regimens and their genetic results.</p>
<a class="btn btn-sample">DOWNLOAD SAMPLE REPORT</a>

<div class="abs report-thumb">
  <svg class="report-page" viewBox="0 0 135 163" aria-label="Sample weight management report page">
    <rect x="45" y="5" width="50" height="3" fill="#333"/>
    <rect x="55" y="10" width="30" height="2" fill="#888"/>
    <rect x="5" y="5" width="18" height="3" fill="#555"/>
    <g fill="#999">
      <rect x="5" y="20" width="30" height="1.5"/><rect x="5" y="24" width="25" height="1.5"/><rect x="5" y="28" width="28" height="1.5"/>
      <rect x="50" y="20" width="30" height="1.5"/><rect x="50" y="24" width="22" height="1.5"/>
      <rect x="95" y="20" width="35" height="1.5"/><rect x="95" y="24" width="30" height="1.5"/><rect x="95" y="28" width="32" height="1.5"/><rect x="95" y="32" width="28" height="1.5"/>
    </g>
    <path d="M5 43 H125 L130 48 L125 53 H5 Z" fill="var(--navy)"/>
    <g stroke="#bbb" stroke-width=".6" fill="none">
      <rect x="5" y="53" width="120" height="35"/>
      <line x1="5" y1="60" x2="125" y2="60"/><line x1="5" y1="67" x2="125" y2="67"/><line x1="5" y1="74" x2="125" y2="74"/><line x1="5" y1="81" x2="125" y2="81"/>
      <line x1="25" y1="53" x2="25" y2="88"/><line x1="40" y1="53" x2="40" y2="88"/><line x1="55" y1="53" x2="55" y2="88"/><line x1="68" y1="53" x2="68" y2="88"/>
    </g>
    <rect x="5" y="93" width="125" height="4" fill="var(--navy)"/>
    <g fill="#aaa">
      <rect x="5" y="101" width="120" height="1.5"/><rect x="5" y="106" width="115" height="1.5"/><rect x="5" y="111" width="120" height="1.5"/><rect x="5" y="116" width="100" height="1.5"/><rect x="5" y="121" width="118" height="1.5"/>
    </g>
    <rect x="5" y="126" width="125" height="4" fill="var(--navy)"/>
    <g fill="#aaa">
      <rect x="5" y="134" width="120" height="1.5"/><rect x="5" y="139" width="118" height="1.5"/><rect x="5" y="144" width="122" height="1.5"/><rect x="5" y="149" width="110" height="1.5"/>
    </g>
    <rect x="5" y="154" width="70" height="1.5" fill="#7a3cc4"/>
  </svg>
</div>

<div class="abs footer-rule"></div>
<footer class="abs footer">©&nbsp; Vantorix All Rights reserved</footer>

</body>
</html>
```